Website for Company to help with House Restoration from Hurricane Damage

Crisp, Clean and Professional!

I need a FRONT page for a website. I need it created in photoshop with the layers intact. We DO NOT need the HTML or DRB for the site. Simply the design. Any fonts you use will need to be included if they are not standard. Please make sure any fonts you use in the body of the text are available for use on Google Fonts.

I have attached a word doc that lists the menu items and additional instructions.

A little about the company - after Hurricane Marlow - DRB developed a system which allows the house to be raised, the Tremlets installed, and the house reset on the Tremlets without the expense of moving the house or driving new pilings. This option can be installed in a matter of days with limited space and at a lower construction cost.

Please refer to the attached musthaves.doc and images that are included.

The main page must incorporate the menu, the attached photos w/ text underneath (text is in the word doc attached), and the text included in the word doc.

Standard footer with contact info as well.

If you have questions please contact us!
Updates

Designs are due by Friday! We will pick one this weekend.  We are unable to change it from 10 days to 5.  Thank you!!!

Target Market(s)

People who lost their homes or businesses due to a hurricane.

Industry/Entity Type

Construction

Requirements
Must have
• See attached musthaves.doc

```html
<!DOCTYPE html>
<html lang="en">
<head>
<meta charset="utf-8">
<title>Durable Raise Builders</title>
<link rel="stylesheet" href="https://fonts.googleapis.com/css2?family=Carlito:wght@400;700&display=swap">
<style>
:root{
  --black:#000;
  --green:#4f7f0a;
  --green-light:#c3d6a0;
  --logo-green:#b9cf8c;
  --page:#f4f4f4;
  --text:#5a5a5a;
  --heading:#111;
  --white:#fff;
  --footer-text:#d0d0d0;
  --footer-link:#6aa21a;
}
*{margin:0;padding:0;box-sizing:border-box}
html,body{width:1200px;height:1093px;overflow:hidden;background:var(--page);font-family:"Carlito",sans-serif}
.site{position:relative;width:1200px;height:1093px}
.hero{position:absolute;left:0;top:0;width:1200px;height:456px;
  background:linear-gradient(180deg,
    #c895a8 0%,#dca0a6 10%,#eea48e 24%,#f6b38a 27%,
    #6f6a78 29%,#9a7f98 34%,#b68fa6 44%,#9b8496 56%,#7f7484 66%,
    #6d6670 72%,#8e8a8e 78%,#a9a5a8 88%,#bdb9bb 100%)}
.slide-arrow{position:absolute;top:226px;width:28px;height:30px;background:#3a3a3a;border-radius:4px;border:1px solid #888;display:flex;align-items:center;justify-content:center}
.slide-arrow.prev{left:11px}.slide-arrow.next{left:1156px}
.header{position:absolute;left:0;top:14px;width:974px;height:87px;background:var(--black)}
.header::after{content:"";position:absolute;right:0;top:0;width:5px;height:87px;background:var(--green)}
.brand{position:absolute;left:229px;top:58px;color:var(--white);font-size:16px;display:flex;align-items:center;gap:8px}
.brand .mark{width:13px;height:13px;background:var(--logo-green)}
.nav{position:absolute;left:440px;top:0;display:flex;height:87px}
.nav a{color:var(--white);text-decoration:none;font-size:12.5px;padding:0 10px;line-height:86px;height:73px}
.nav a.active{background:var(--green);color:var(--heading)}
.tagline{position:absolute;left:0;top:456px;width:1200px;height:34px;background:var(--black)}
.tagline svg{position:absolute;left:0;top:0}
.tagline span{position:absolute;top:8px;font-size:15px}
.t1{left:259px;color:var(--heading)}.t2{left:478px;color:var(--heading)}.t3{left:655px;color:var(--white)}
.intro{position:absolute;left:229px;top:530px;width:742px}
.intro h1{font-size:15.5px;font-weight:400;color:var(--heading)}
.photo{position:absolute;left:0;top:33px;width:276px;height:150px;border:3px solid var(--white);box-shadow:2px 2px 4px rgba(0,0,0,.35);
  background:linear-gradient(180deg,#c9d3dc 0%,#a7b4bd 12%,#3f5a2e 22%,#8a2f2c 34%,#a5352f 55%,#8d2e2a 72%,#567d32 86%,#3c5b22 100%)}
.intro p{font-size:12px;line-height:19px;color:var(--text);text-align:justify}
.p1{position:absolute;left:288px;top:32px;width:452px}
.p2{position:absolute;left:1px;top:198px;width:741px}
.read-more{position:absolute;left:867px;top:822px;width:103px;height:31px;background:var(--green);color:var(--white);font-size:11px;text-decoration:none;display:flex;align-items:center;justify-content:center;letter-spacing:.3px}
.footer{position:absolute;left:0;top:897px;width:1200px;height:196px;background:var(--black);border-top:5px solid var(--green)}
.footer-brand{position:absolute;left:257px;top:48px;width:200px;color:var(--white);font-size:15px;line-height:18px;display:flex;align-items:flex-start;gap:9px}
.footer-brand .mark{flex:none;width:13px;height:13px;margin-top:3px;background:var(--logo-green)}
.contact{position:absolute;left:258px;top:88px;font-size:12px;line-height:21.5px;color:var(--footer-text)}
.contact b{font-weight:400;color:var(--footer-link)}
.sitemap{position:absolute;left:783px;top:43px;color:var(--footer-text)}
.sitemap h2{font-size:15px;font-weight:400;margin-bottom:4px}
.sitemap ul{list-style:none;margin-left:15px;font-size:11px;line-height:13.7px}
.sitemap li::before{content:":: ";color:#888}
</style>
</head>
<body>
<div class="site">
  <div class="hero" role="img" aria-label="Sunset beach photograph of a parent and child at the water's edge with boats on the bay"></div>
  <div class="slide-arrow prev"><svg width="12" height="16" viewBox="0 0 12 16"><path d="M9 2 3 8l6 6" fill="none" stroke="#fff" stroke-width="2.5"/></svg></div>
  <div class="slide-arrow next"><svg width="12" height="16" viewBox="0 0 12 16"><path d="M3 2l6 6-6 6" fill="none" stroke="#fff" stroke-width="2.5"/></svg></div>

  <header class="header">
    <div class="brand"><span class="mark"></span>Durable Raise Builders</div>
    <nav class="nav">
      <a class="active" href="#">Home</a>
      <a href="#">Services</a>
      <a href="#">About us</a>
      <a href="#">Product Specifications</a>
      <a href="#">Design Documentation</a>
      <a href="#">Contact Us</a>
    </nav>
  </header>

  <div class="tagline">
    <svg width="620" height="34" viewBox="0 0 620 34">
      <polygon points="0,0 410,0 420,17 410,34 0,34" fill="#c3d6a0"/>
      <polygon points="410,0 605,0 617,17 605,34 410,34 420,17" fill="#4f7f0a"/>
    </svg>
    <span class="t1">REBUILD SAFER</span>
    <span class="t2">STRONGER</span>
    <span class="t3">BETTER TO BUILD NEW LASTING MEMORIES</span>
  </div>

  <section class="intro">
    <h1>Durable Raise Builders, LLC (DRB)</h1>
    <div class="photo" role="img" aria-label="Photograph of a red two-storey house with white trim and trees"></div>
    <p class="p1">Systems for extending the height of existing piles are not available on today’s market. Durable Raise Builders, LLC (DRB) has developed two systems to allow for Piles to be extended that provide superior structural support without corrosion and maintenance concerns. We provided two systems, a complete system, Pile Cap Extension Tremlets, and Pile Splice. These two systems allow a home to be raised to by up to 54”, higher extensions possible with additional design consideration for lateral support. Shown below is the full Piling Extension system, which connects to the top of the existing pile. The system modular and can be cut to meet specific needs of the home.</p>
    <p class="p2">Our Patented Piling system has been designed to withstand the corrosive environment of beach communities. The salt water and windblown sand corrodes unprotected materials, and yes, even stainless steel. Our system utilizes a high strength carbon fiber material that is corrosion proof from salt water and UV proof. The system will not erode, decay or loose strength over time. The system has three installation conditions, for raising a house on existing pilings, repairing damaged pilings, and for connecting new pilings to floor joists in new construction. The three options are generally described here.</p>
  </section>
  <a class="read-more" href="#">READ MORE &gt;&gt;</a>

  <footer class="footer">
    <div class="footer-brand"><span class="mark"></span>Durable Raise Builders, LLC (DRB)</div>
    <div class="contact">
      P.O. Box : <b>40512, Harbor Glen,</b><br>
      PA : <b>18990-0120 - (555) 014-2286</b><br>
      Email : <b>sales@durableraise.example</b>
    </div>
    <div class="sitemap">
      <h2>Site Map</h2>
      <ul>
        <li>Home</li><li>Services</li><li>About Us</li><li>Product Specifications</li><li>Design Documentation</li><li>Contact Us</li>
      </ul>
    </div>
  </footer>
</div>
</body>
</html>
```